Fresh Tarrow Work Post - Business Card Required

Dear All,

I own Velmira Limited, which in turn owns the website:
www.harbinworkpost.example

I want all of you wonderful creative people to come up with a slick, and awesome business card design that incorporates the logo on the site, and some colouring and design elements from it.

You have free reign in how you go about doing this, I won't be giving my contact details on this platform, but the winner will be asked to redesign based on my contact details which I will supply at the end.

I need the design to be completed within 5 days. I need the final print copies of the business cards by the 25th November, so unfortunately it's a bit of a rush to get these designs ready.

Any questions, please ask.

Thank you
Updates

Thank you all for your hard work and exceptional designs provided. I do have to pick one, so I have a very clear idea of which one this is, however I will wait one further day until the competition closes to be fair to all those have submitted, or are in the process of submitting. I wish you all the best and thank you again for your dedication.

```html
<!DOCTYPE html>
<html lang="en">
<head>
<meta charset="utf-8">
<title>Harbin Work Post – Business Card</title>
<link rel="stylesheet" href="https://fonts.googleapis.com/css2?family=Arimo:wght@400;500&display=swap">
<style>
  :root {
    --page-bg: #ececec;
    --card-centre: #2b2b2b;
    --card-edge: #0b0b0b;
    --text-light: #f2f2f2;
    --brand-gold: #d2a93f;
    --gold-deep: #a9791f;
    --gold-bright: #f1d27a;
    --silver-light: #f4f4f4;
    --silver-mid: #b9b9b9;
  }
  * { margin: 0; padding: 0; box-sizing: border-box; }
  html, body {
    width: 1066px;
    height: 1200px;
    overflow: hidden;
    background: var(--page-bg);
    font-family: "Arimo", Arial, sans-serif;
  }
  .canvas {
    position: relative;
    width: 1066px;
    height: 1200px;
  }
  .card {
    position: absolute;
    left: 162px;
    width: 754px;
    height: 444px;
    overflow: hidden;
    background: radial-gradient(ellipse at 55% 40%, var(--card-centre) 0%, var(--card-edge) 85%);
  }
  .card--front { top: 92px; }
  .card--back { top: 656px; }

  /* front */
  .brand-mark {
    position: absolute;
    left: 66px;
    top: 150px;
    display: flex;
    align-items: center;
    gap: 10px;
    color: var(--brand-gold);
    font-size: 17px;
    font-weight: 500;
    letter-spacing: 1.5px;
    text-transform: uppercase;
  }
  .brand-mark__dot {
    width: 14px;
    height: 14px;
    border-radius: 50%;
    background: var(--brand-gold);
  }
  .contact {
    position: absolute;
    right: 58px;
    top: 202px;
    text-align: right;
    color: var(--text-light);
  }
  .contact__name { font-size: 24px; font-weight: 400; line-height: 1.1; }
  .contact__role { font-size: 12.5px; margin-top: 3px; }
  .contact__details {
    list-style: none;
    margin-top: 22px;
    font-size: 16.5px;
    line-height: 18px;
  }
  .swoosh {
    position: absolute;
    left: 0;
    top: 0;
    width: 754px;
    height: 444px;
  }

  /* back */
  .brand-centre {
    position: absolute;
    inset: 0;
    display: flex;
    align-items: center;
    justify-content: center;
    gap: 18px;
    color: var(--brand-gold);
    font-size: 38px;
    font-weight: 500;
    letter-spacing: 4px;
    text-transform: uppercase;
  }
  .brand-centre__dot {
    width: 28px;
    height: 28px;
    border-radius: 50%;
    background: var(--brand-gold);
  }
</style>
</head>
<body>
<main class="canvas">
  <section class="card card--front" aria-label="Business card front">
    <div class="brand-mark">
      <span class="brand-mark__dot"></span>
      <span>Harbin Work Post</span>
    </div>

    <div class="contact">
      <p class="contact__name">Corwen Marsh</p>
      <p class="contact__role">Managing Director</p>
      <ul class="contact__details">
        <li>0700 555 0148</li>
        <li>contact@harbinworkpost.example</li>
        <li>www.harbinworkpost.example</li>
        <li>17 Ferrow Lane, Tarrow, TR4 8QJ</li>
      </ul>
    </div>

    <svg class="swoosh" viewBox="0 0 754 444" aria-hidden="true">
      <defs>
        <linearGradient id="silverBand" x1="0" y1="0" x2="1" y2="0">
          <stop offset="0" stop-color="var(--silver-mid)"/>
          <stop offset="0.35" stop-color="var(--silver-light)"/>
          <stop offset="0.7" stop-color="var(--silver-mid)"/>
          <stop offset="1" stop-color="var(--silver-light)"/>
        </linearGradient>
        <linearGradient id="goldBand" x1="0" y1="0" x2="1" y2="0">
          <stop offset="0" stop-color="var(--gold-deep)"/>
          <stop offset="0.45" stop-color="var(--gold-bright)"/>
          <stop offset="0.75" stop-color="var(--brand-gold)"/>
          <stop offset="1" stop-color="var(--gold-deep)"/>
        </linearGradient>
      </defs>
      <path d="M0 328 C 180 370, 420 420, 754 428 L754 444 L0 444 Z" fill="url(#silverBand)"/>
      <path d="M0 364 C 200 400, 440 432, 754 440 L754 444 L0 444 Z" fill="url(#goldBand)"/>
    </svg>
  </section>

  <section class="card card--back" aria-label="Business card back">
    <div class="brand-centre">
      <span class="brand-centre__dot"></span>
      <span>Harbin Work Post</span>
    </div>
  </section>
</main>
</body>
</html>
```